Profesional personal website needs design and business card

I need a business card with my professional name as a logo "Marlo Vitality" for my business. I am a Wellness Coach, consultant and trainer. So it should be professional, wellness oriented and modern.

Target Market(s)

Private clients, governments, corporations. Luxury and high market.

Industry/Entity Type

Health And Wellness

Contact Information for Business Card

Marlo Vitality should be the logo

Colors

Designer to choose colors to be used in the design.

Requirements
Must have
• Marlo Vitality
• Name: Tomás Arribal
• Wellness Coach, Consultant & Trainer.
• Website: www.marlovitality.example
• Phone:
• Spain (+34) 612 480 397
• (USA) +1 (555) 318 2046
Nice to have
• The most important is the design of "Marlo Vitality", as this is going to be my personal brand logo. It should be professional, wellness, high end and actual.
Should not have
• no golds, no baroque style..

```html
<!DOCTYPE html>
<html lang="en">
<head>
<meta charset="utf-8">
<title>Marlo Vitality – Business Card</title>
<link rel="stylesheet" href="https://fonts.googleapis.com/css2?family=Lato:wght@400;700;900&display=swap">
<style>
  :root {
    --brand-blue: #04729a;
    --name-blue: #0a6f98;
    --ink: #2f3336;
    --muted: #4a4f54;
    --paper: #ffffff;
    --page: #ffffff;
    --shadow: rgba(0, 0, 0, 0.28);
  }
  * { box-sizing: border-box; margin: 0; padding: 0; }
  html, body {
    width: 1200px; height: 1200px; overflow: hidden;
    background: var(--page);
    font-family: "Lato", sans-serif;
  }
  .stage { position: relative; width: 1200px; height: 1200px; }

  .card {
    position: absolute; left: 180px; width: 840px; height: 477px;
    box-shadow: 5px 6px 6px var(--shadow);
  }
  .card--front { top: 84px; background: var(--paper); }
  .card--back { top: 640px; background: var(--brand-blue); }

  .wordmark {
    position: absolute; text-align: center;
    font-family: "Lato", sans-serif; font-weight: 900; line-height: 1;
  }
  .wordmark__main { display: block; letter-spacing: 0.06em; }
  .wordmark__sub { display: block; letter-spacing: 0.32em; }

  .card--front .wordmark { left: 72px; top: 198px; width: 312px; color: var(--brand-blue); }
  .card--front .wordmark__main { font-size: 58px; }
  .card--front .wordmark__sub { font-size: 22px; margin-top: 10px; padding-left: 0.32em; }

  .card--back .wordmark { left: 202px; top: 190px; width: 436px; color: #ffffff; }
  .card--back .wordmark__main { font-size: 82px; }
  .card--back .wordmark__sub { font-size: 31px; margin-top: 14px; padding-left: 0.32em; }

  .divider {
    position: absolute; left: 419px; top: 154px; width: 3px; height: 165px;
    background: var(--brand-blue);
  }

  .identity { position: absolute; left: 460px; top: 150px; }
  .identity__name {
    font-size: 39px; font-weight: 700; color: var(--name-blue); letter-spacing: -0.01em; line-height: 1.1;
  }
  .identity__role { font-size: 19.5px; color: var(--muted); margin-top: 1px; }

  .contacts { position: absolute; left: 460px; top: 236px; list-style: none; }
  .contacts li {
    display: flex; align-items: center; height: 29px;
    font-size: 19.5px; color: var(--ink);
  }
  .contacts li + li { margin-top: 0.5px; }
  .contacts svg { width: 20px; height: 20px; margin-right: 7px; flex: none; }
  .contacts .region { color: var(--brand-blue); margin-left: 5px; }

  .back-url {
    position: absolute; left: 0; right: 0; top: 423px; text-align: center;
    color: #ffffff; font-size: 19.5px;
  }
</style>
</head>
<body>
<main class="stage">
  <section class="card card--front" aria-label="Card front">
    <div class="wordmark">
      <span class="wordmark__main">MARLO</span>
      <span class="wordmark__sub">VITALITY</span>
    </div>
    <div class="divider"></div>
    <div class="identity">
      <h1 class="identity__name">Tomás Arribal</h1>
      <p class="identity__role">Wellness Coach, Consultant &amp; Trainer</p>
    </div>
    <ul class="contacts">
      <li>
        <svg viewBox="0 0 24 24" aria-hidden="true"><path fill="#04729a" d="M6.6 2.5c.6-.3 1.3-.1 1.6.5l2 3.6c.3.6.2 1.3-.3 1.7L8.4 9.6c1.1 2.5 3.1 4.7 5.7 6l1.4-1.5c.4-.5 1.1-.6 1.7-.3l3.6 2c.6.3.8 1 .5 1.6l-1.2 2.6c-.4.8-1.3 1.3-2.2 1.1C10.4 19.6 4.4 13.6 2.9 6.1c-.2-.9.3-1.8 1.1-2.2z"/></svg>
        (+34) 612 480 397<span class="region">Spain</span>
      </li>
      <li>
        <svg viewBox="0 0 24 24" aria-hidden="true"><rect x="7" y="2" width="10" height="20" rx="2" fill="none" stroke="#04729a" stroke-width="2"/><circle cx="12" cy="18.5" r="1.3" fill="#04729a"/></svg>
        +1 (555) 318 2046<span class="region">(USA)</span>
      </li>
      <li>
        <svg viewBox="0 0 24 24" aria-hidden="true"><circle cx="12" cy="12" r="9" fill="none" stroke="#04729a" stroke-width="2"/><path d="M3 12h18M12 3c3 3 3 15 0 18M12 3c-3 3-3 15 0 18" fill="none" stroke="#04729a" stroke-width="1.5"/></svg>
        www.marlovitality.example
      </li>
    </ul>
  </section>

  <section class="card card--back" aria-label="Card back">
    <div class="wordmark">
      <span class="wordmark__main">MARLO</span>
      <span class="wordmark__sub">VITALITY</span>
    </div>
    <p class="back-url">www.marlovitality.example</p>
  </section>
</main>
</body>
</html>
```